Fundvane Informational Banners for Ashen Tide Rising

Hello, We are currently in the Process of doing a Fundvane Campaign which is due on the 4th. We need a Grungy/Dirty Dark Dead Feeling set of Banners, and Informational Pieces in Various Sizes.
Banner Sizes:
640px × 88px Normall Banner
640px × 57px Breaker Banner
700px × 93px Header Banner
640px × 635px Display Box for Rewards
A Larger box, that needs to have a Seamless beginning and ending also needs to be made, so it can be extended as more text and so-forth is completed.

We are looking for very Dead, Dark looking images, thesr are ment to be displayed on the fundvane webpage they need to flow well with the fundvane form, as well as show off our things, simple or advanced. They need to match our style.

NOTE IMPORTANT!!!!
THESE ARE NOT ADVERTISING BANNERS, THESE ARE BANNERS FOR THE FUNDVANE WEBSITE FOR A CAMPAIGN PLEASE DO SOME HOMEWORK BEFORE ATTEMPTING THESE IMAGES WE ARE NOT LOOKING FOR ADVERTISING BANNERS WE ARE LOOKING FOR INFORMATIONAL PIECES

Example of words that will be used on the various Banners

"Physical Add-ons"
"Digital Add-ons"
"Who we are"
"What is Ashen Tide Rising?"
"What is Procedural Generation?"
"Why are you Attempting this?"

THESE ARE EXAMPLE SENTENCES THAT WILL BE IN THE BANNERS I REPEAT THESE ARE NOT ADVERTISING WEBBANNERS
Updates

Everyone is Doing wonderful, thank you all for making such lovely work. thank You. Keep it up, remember undead feel, it must be functional piece on the fundvane website. :3 

Target Market(s)

Zombie, and Undead ages People 13-51 that are Gamers

Industry/Entity Type

Digital

Requirements
Must have
• These Designs must be Boxes and Banners, and Break Points for a Fundvane Information Display I will provide a few links here.
http://www.fundvane-example.com/projects/brevmoor/harrow-veils-of-quillan
http://www.fundvane-example.com/projects/corvale/venture-paragon

Our Artwork Style & Concept Artwork can be found here
http://www.gamevault-example.net/games/ashen-tide-rising/images

```html
<!DOCTYPE html>
<html lang="en">
<head>
<meta charset="utf-8">
<title>Ashen Tide Rising — Fundvane Information Banners</title>
<link rel="stylesheet" href="https://fonts.googleapis.com/css2?family=Silkscreen:wght@400;700&display=swap">
<style>
  :root {
    --page: #ffffff;
    --void: #0a0706;
    --soot: #15100d;
    --dried-blood: #4a0b09;
    --blood: #8e130f;
    --fresh-blood: #c4160f;
    --rot-tan: #7a5a3a;
    --bone: #e8e0d2;
  }
  * { margin: 0; padding: 0; box-sizing: border-box; }
  html, body { width: 1200px; height: 600px; overflow: hidden; background: var(--page); }
  .canvas { position: relative; width: 1200px; height: 600px; background: var(--page); }
  .filter-defs { position: absolute; width: 0; height: 0; }

  .banner { position: absolute; overflow: hidden; background: var(--void); }
  .banner__art, .banner__grime, .banner__shade { position: absolute; inset: 0; width: 100%; height: 100%; }
  .banner__title {
    position: absolute;
    top: 50%;
    transform: translateY(-50%);
    font-family: "Silkscreen", monospace;
    font-weight: 700;
    color: var(--bone);
    text-transform: uppercase;
    white-space: nowrap;
    letter-spacing: 2px;
    text-shadow: 0 0 4px rgba(0,0,0,.95), 0 0 1px #000;
  }

  /* Header banner 700×93 */
  .banner--header { left: 87px; top: 45px; width: 1050px; height: 138px; }
  .banner--header .banner__art {
    background:
      radial-gradient(ellipse 20% 60% at 87% 48%, #6b3a2c 0%, rgba(60,20,14,.6) 55%, transparent 80%),
      radial-gradient(ellipse 35% 70% at 45% 80%, rgba(142,19,15,.85) 0%, transparent 70%),
      linear-gradient(90deg, var(--soot) 0%, var(--dried-blood) 35%, var(--blood) 55%, #3a1a12 75%, var(--soot) 100%);
  }
  .banner--header .banner__shade { background: linear-gradient(90deg, rgba(8,5,4,.85) 0%, rgba(8,5,4,.55) 45%, transparent 65%); }
  .banner--header .banner__title { left: 55px; font-size: 25px; }

  /* Normal banner 640×88 */
  .banner--normal { left: 120px; top: 235px; width: 960px; height: 130px; }
  .banner--normal .banner__art {
    background:
      radial-gradient(ellipse 8% 28% at 62% 72%, var(--fresh-blood) 0%, rgba(196,22,15,.6) 55%, transparent 85%),
      radial-gradient(ellipse 30% 60% at 78% 35%, rgba(122,90,58,.75) 0%, transparent 75%),
      linear-gradient(90deg, #3a2a1a 0%, var(--soot) 10%, var(--void) 45%, var(--dried-blood) 62%, var(--blood) 80%, #3a2418 100%);
  }
  .banner--normal .banner__shade { background: radial-gradient(ellipse 38% 42% at 36% 50%, rgba(6,4,3,.95) 0%, rgba(6,4,3,.8) 70%, transparent 100%); }
  .banner--normal .banner__title { left: 63px; font-size: 18px; color: #d8cdb8; }

  /* Breaker banner 640×57 */
  .banner--breaker { left: 120px; top: 411px; width: 960px; height: 86px; }
  .banner--breaker .banner__art {
    background: linear-gradient(90deg, var(--blood) 0%, var(--void) 6%, var(--soot) 26%, var(--blood) 42%, var(--dried-blood) 65%, var(--blood) 85%, var(--dried-blood) 100%);
  }
  .banner--breaker .banner__shade { background: linear-gradient(90deg, transparent 0%, rgba(8,5,4,.7) 5%, rgba(8,5,4,.75) 30%, transparent 42%); }
  .banner--breaker .banner__title { left: 37px; font-size: 19px; }

  .banner__edge { position: absolute; left: 0; right: 0; height: 10px; background: var(--void); opacity: .9; }
  .banner__edge--top { top: 0; }
  .banner__edge--bottom { bottom: 0; }
</style>
</head>
<body>
<svg class="filter-defs" aria-hidden="true">
  <defs>
    <filter id="blood-blotch" x="0" y="0" width="100%" height="100%">
      <feTurbulence type="fractalNoise" baseFrequency="0.012 0.05" numOctaves="5" seed="4"/>
      <feColorMatrix values="0 0 0 0 0.55  0 0 0 0 0.06  0 0 0 0 0.05  4.2 0 0 0 -1.9"/>
    </filter>
    <filter id="rot-blotch" x="0" y="0" width="100%" height="100%">
      <feTurbulence type="fractalNoise" baseFrequency="0.02 0.07" numOctaves="5" seed="11"/>
      <feColorMatrix values="0 0 0 0 0.46  0 0 0 0 0.33  0 0 0 0 0.21  4 0 0 0 -2.05"/>
    </filter>
    <filter id="soot-stain" x="0" y="0" width="100%" height="100%">
      <feTurbulence type="fractalNoise" baseFrequency="0.03 0.1" numOctaves="4" seed="23"/>
      <feColorMatrix values="0 0 0 0 0.03  0 0 0 0 0.02  0 0 0 0 0.02  4 0 0 0 -1.8"/>
    </filter>
    <filter id="grit" x="0" y="0" width="100%" height="100%">
      <feTurbulence type="fractalNoise" baseFrequency="0.85" numOctaves="3" seed="7"/>
      <feColorMatrix values="0 0 0 0 0.02  0 0 0 0 0.01  0 0 0 0 0.01  3.2 0 0 0 -1.3"/>
    </filter>
    <filter id="flecks" x="0" y="0" width="100%" height="100%">
      <feTurbulence type="fractalNoise" baseFrequency="0.6" numOctaves="2" seed="31"/>
      <feColorMatrix values="0 0 0 0 0.75  0 0 0 0 0.62  0 0 0 0 0.45  0 6 0 0 -3.7"/>
    </filter>
  </defs>
</svg>

<main class="canvas">
  <section class="banner banner--header">
    <div class="banner__art" role="img" aria-label="Grunge texture of dark blood splatter fading into a close-up of an undead creature on the right"></div>
    <svg class="banner__grime" aria-hidden="true" preserveAspectRatio="none">
      <rect width="100%" height="100%" filter="url(#blood-blotch)"/>
      <rect width="100%" height="100%" filter="url(#rot-blotch)" opacity=".8"/>
      <rect width="100%" height="100%" filter="url(#soot-stain)"/>
      <rect width="100%" height="100%" filter="url(#flecks)" opacity=".5"/>
      <rect width="100%" height="100%" filter="url(#grit)"/>
    </svg>
    <div class="banner__shade"></div>
    <div class="banner__edge banner__edge--top"></div>
    <h1 class="banner__title">What is Ashen Tide Rising?</h1>
  </section>

  <section class="banner banner--normal">
    <div class="banner__art" role="img" aria-label="Grungy black and rust texture with a bloody handprint splatter"></div>
    <svg class="banner__grime" aria-hidden="true" preserveAspectRatio="none">
      <rect width="100%" height="100%" filter="url(#rot-blotch)"/>
      <rect width="100%" height="100%" filter="url(#blood-blotch)" opacity=".8"/>
      <rect width="100%" height="100%" filter="url(#soot-stain)"/>
      <rect width="100%" height="100%" filter="url(#flecks)" opacity=".6"/>
      <rect width="100%" height="100%" filter="url(#grit)"/>
    </svg>
    <div class="banner__shade"></div>
    <div class="banner__edge banner__edge--top"></div>
    <div class="banner__edge banner__edge--bottom"></div>
    <h2 class="banner__title">Why are you attempting this</h2>
  </section>

  <section class="banner banner--breaker">
    <div class="banner__art" role="img" aria-label="Dark red grunge texture of torn, bloodied flesh"></div>
    <svg class="banner__grime" aria-hidden="true" preserveAspectRatio="none">
      <rect width="100%" height="100%" filter="url(#blood-blotch)"/>
      <rect width="100%" height="100%" filter="url(#soot-stain)"/>
      <rect width="100%" height="100%" filter="url(#flecks)" opacity=".3"/>
      <rect width="100%" height="100%" filter="url(#grit)"/>
    </svg>
    <div class="banner__shade"></div>
    <div class="banner__edge banner__edge--top"></div>
    <h2 class="banner__title">Physical Add-ons</h2>
  </section>
</main>
</body>
</html>
```